New Zealand Luggage Importer Needs Business Cards

We need professional, creative and fashionable business cards created.
We are based in New Zealand and import and distribute high-end, quality, fashionable and durable luggage.
We pride ourselves on selling the very best quality luggage, second only to 1 brand (which we won't mention here)...we use the same manufacturer. However, our prices are much more reasonable.
Industry/Entity Type
Business
Contact Information for Business Card
Mark Dunsley
027 512 4068
3/17 Harlow Street, Pinecrest Flats, Auckland, 0614
PO Box 204377, Fernside, Auckland 0731
09-528-3916
sales@brivancases.co.nz / www.brivancases.co.nz

```html
<!DOCTYPE html>
<html lang="en">
<head>
<meta charset="utf-8">
<title>Brivan Cases – Business Card</title>
<link rel="stylesheet" href="https://fonts.googleapis.com/css2?family=Montserrat:wght@500;600;700&display=swap">
<style>
  :root {
    --backdrop: #e2dca8;
    --gold-deep: #c09a4a;
    --gold-mid: #d9bf60;
    --gold-light: #ebe077;
    --ink: #1d1a1a;
    --band: #1c1919;
    --logo: #ffffff;
    --rule: #b08a40;
  }
  * { margin: 0; padding: 0; box-sizing: border-box; }
  html, body {
    width: 1200px; height: 1200px; overflow: hidden;
    background: var(--backdrop);
    font-family: "Montserrat", Arial, sans-serif;
    color: var(--ink);
  }
  .sheet {
    width: 1200px; height: 1200px;
    display: flex; flex-direction: column;
    align-items: center; justify-content: center;
    gap: 60px;
  }
  .card {
    position: relative;
    width: 860px; height: 513px;
    background: linear-gradient(120deg, var(--gold-deep) 0%, var(--gold-mid) 28%, var(--gold-light) 52%, var(--gold-mid) 76%, var(--gold-deep) 100%);
    box-shadow: 0 6px 18px rgba(60, 50, 10, 0.28);
    overflow: hidden;
  }
  .brand-band {
    position: absolute; left: 0; right: 0;
    top: 361px; height: 103px;
    background: var(--band);
    display: flex; align-items: center;
    padding-left: 100px;
  }
  .brand-name {
    font-weight: 700; font-size: 58px;
    letter-spacing: 2px; color: var(--logo);
    line-height: 1;
  }
  .holder-name {
    position: absolute; left: 92px; top: 78px;
    font-size: 37px; font-weight: 600; letter-spacing: 0.5px;
  }
  .contact-list {
    position: absolute; left: 88px; top: 140px;
    list-style: none; font-size: 21px; font-weight: 500;
    line-height: 31px;
  }
  .contact-list b { font-weight: 700; }
  .contact-list .indent { padding-left: 31px; }
  .divider {
    position: absolute; left: 584px; top: 89px;
    width: 1px; height: 211px; background: var(--rule);
  }
  .address {
    position: absolute; left: 657px;
    font-size: 21px; font-weight: 500; line-height: 29px;
    font-style: normal;
  }
  .address.street { top: 80px; }
  .address.postal { top: 212px; }
  .web-address {
    position: absolute; left: 313px; top: 298px;
    font-size: 20px; font-weight: 500;
  }
</style>
</head>
<body>
<main class="sheet">
  <section class="card card-front" aria-label="Business card front">
    <h1 class="holder-name">MARK DUNSLEY</h1>
    <ul class="contact-list">
      <li><b>E:</b> sales@brivancases.co.nz</li>
      <li><b>W:</b> brivancases.co.nz</li>
      <li><b>P:</b> 027 512 4068</li>
      <li class="indent">09-528-3916</li>
    </ul>
    <div class="divider"></div>
    <address class="address street">3/17 Harlow Street,<br>Pinecrest Flats,<br>Auckland, 0614</address>
    <address class="address postal">PO Box 204377,<br>Fernside,<br>Auckland 0731</address>
    <div class="brand-band"><span class="brand-name">BRIVAN CASES</span></div>
  </section>

  <section class="card card-back" aria-label="Business card back">
    <p class="web-address">www.brivancases.co.nz</p>
    <div class="brand-band"><span class="brand-name">BRIVAN CASES</span></div>
  </section>
</main>
</body>
</html>
```